Ashworth Web Design Project

I need the front page and an internal page designed for this client's website. The logo is attached. Obviously the colors have to go with and/or work with the logo colors. I also attached a very rough brochure layout to help you see the direction we're going in with print materials. The rough site map is also attached. I see a slider on the homepage, the art for which I may come back to you to create. This clinic is in a very high end Dallas neighborhood. The hook is that it's a primary care and urgent facility with convenient hours.

I don't know how much this impacts your design, but this will be a Wordpress site and I'm using a framework called Struxo (struxo-demo.example). If Struxo proves to be inflexible, I'll have to get a template that allows me to execute your design.

This site (http://oakbendcareclinic.example) has the type and quality of content I will eventually have on the Ashworth site.

I just revised the brief for this project. I added the site map and added details to the overview and the "Must Have" section. Thank you for revisiting the brief. 

Reason: Christmas was a bad time to end it.

Target Market(s)

Women 25-54 with children living at home, income over $150k/year

Industry/Entity Type

Clinic

Requirements
Must have
• Masthead incorporating the logo
Followed by the primary nav
Slider on the home page below that
Dual nav - 1 with the nav in the attached site map
2 secondary nav with areas of healthcare
There will three blocks under the nav
1. It's about time (with a small blurb less than 50 words.
2. It's about choices (with small blurb)
3. It's about you (with small blurb)
Three footer blocks
patient check in link on every page
"No appointment? No problem" icon on every page

```html
<!DOCTYPE html>
<html lang="en">
<head>
<meta charset="utf-8">
<title>Ashworth Medical – Home</title>
<link href="https://fonts.googleapis.com/css2?family=Open+Sans:wght@400;600;700&family=Delius&display=swap" rel="stylesheet">
<style>
:root{
  --blue:#0d60a5;
  --blue-dark:#0a4f8c;
  --blue-light:#1d8fe6;
  --green:#22b35e;
  --green-soft:#3dbd6e;
  --green-bar:#1ab058;
  --text:#333;
  --muted:#555;
  --white:#fff;
}
*{margin:0;padding:0;box-sizing:border-box}
html,body{width:1200px;height:1200px;overflow:hidden;background:var(--white)}
body{position:relative;font-family:"Open Sans",Arial,sans-serif;color:var(--text)}
.abs{position:absolute}
a{color:inherit}

/* masthead */
.brand{left:130px;top:28px;display:flex;align-items:center;gap:8px}
.brand-mark{width:40px;height:40px;border-radius:50%;background:var(--blue)}
.brand-name{font-size:23px;font-weight:700;color:var(--blue);letter-spacing:-.5px;line-height:1}
.brand-tag{font-size:8px;color:#444;font-weight:600;margin-top:3px;padding-left:24px}
.util-links{right:130px;top:18px;font-size:11px;color:#555;display:flex;gap:9px}

/* nav */
.main-nav{left:0;top:100px;width:1200px;height:34px;background:var(--blue)}
.main-nav ul{list-style:none;display:flex;position:absolute;left:130px;top:0;height:34px}
.main-nav li{font-size:10.5px;font-weight:700;color:var(--white);padding:0 12px;line-height:34px;text-transform:uppercase}
.main-nav li.active{background:var(--green);padding:0 10px;margin-right:7px}

/* slider */
.slider-bg{left:0;top:134px;width:1200px;height:240px;background:linear-gradient(#eee,#fafafa 60%,#e9e9e9);border-bottom:1px solid #ddd}
.slide-photo{left:130px;top:134px;width:581px;height:240px;background:linear-gradient(90deg,#d9d4cc,#c2a98e 35%,#8a8f99 60%,#c9b49a 85%,#e3dbd1)}
.slide-panel{left:711px;top:134px;width:359px;height:240px;background:var(--green);overflow:hidden;color:var(--white)}
.slide-panel h2{position:absolute;left:29px;top:17px;font-size:16px;font-weight:600;text-transform:uppercase}
.slide-panel p{position:absolute;left:29px;top:48px;width:300px;font-size:12.2px;line-height:16.8px}
.slide-btn{position:absolute;left:30px;top:166px;width:102px;height:29px;border:2px solid var(--white);border-radius:15px;font-size:12px;font-weight:700;line-height:25px;padding-left:36px}
.slide-btn svg{position:absolute;left:5px;top:4px}

/* sidebar */
.care-box{left:130px;top:410px;width:220px;height:320px;background:linear-gradient(var(--blue-light),var(--blue) 60%,var(--blue-dark));box-shadow:0 0 3px rgba(0,0,0,.3)}
.care-photo{position:absolute;left:0;top:0;width:220px;height:95px}
.care-box h3{position:absolute;left:31px;top:114px;font-size:12px;font-weight:700;color:var(--white)}
.care-box ul{position:absolute;left:31px;top:137px;list-style:none}
.care-box li{font-size:12.5px;color:var(--white);height:24px;display:flex;align-items:center;gap:9px}
.care-box li::before{content:"»";font-weight:700;font-size:14px;margin-top:-2px}

/* intro */
.intro-title{left:370px;top:406px;font-size:16px;font-weight:600;color:var(--blue)}
.intro-photo{left:370px;top:450px;width:220px;height:110px;background:linear-gradient(#5f8fc4,#a9c3de 45%,#b8b6b0 70%,#7d8a6a);box-shadow:0 6px 6px -4px rgba(0,0,0,.35)}
.intro-text{left:610px;top:447px;width:460px;font-family:Arial,Helvetica,sans-serif;font-size:12px;line-height:14.5px;color:var(--text)}
.intro-text p{margin-bottom:9px}
.intro-text p:first-child{text-indent:36px}

/* about columns */
.about-col{top:596px;width:220px}
.about-col h4{font-family:"Delius",cursive;font-weight:400;font-size:15px;color:var(--blue);height:26px;border-bottom:2px solid var(--green);position:relative}
.about-col h4::after{content:"";position:absolute;left:0;bottom:-2px;width:40px;height:2px;background:var(--blue)}
.about-col p{font-family:Arial,Helvetica,sans-serif;font-size:12px;line-height:14.5px;margin-top:15px}
.about-col p+p{margin-top:8px}

/* feature links */
.feature{top:800px;width:301px;height:62px}
.feature h5{position:absolute;left:0;top:6px;font-size:13.5px;font-weight:700;color:var(--green)}
.feature .rule{position:absolute;left:0;top:29px;width:301px;height:2px;background:var(--green)}
.feature p{position:absolute;left:1px;top:37px;width:225px;font-family:Arial,Helvetica,sans-serif;font-size:12px;line-height:14.5px;color:var(--muted)}
.feature svg{position:absolute;left:230px;top:0}

/* footer */
.footer{left:130px;top:920px;width:940px;height:150px;background:var(--green-soft);color:var(--white)}
.foot-col{position:absolute;top:18px;font-size:11.5px;line-height:16px}
.foot-col h6{font-size:12px;font-weight:700;text-transform:uppercase;margin-bottom:12px}
.foot-sep{position:absolute;top:10px;width:0;height:140px;border-left:1px dotted rgba(255,255,255,.8)}
.social{display:flex;align-items:center;gap:19px;margin-bottom:8px}
.social-icon{width:26px;height:26px;border-radius:3px;background:#3e6cb3;flex:none}
.social-icon.alt{background:#3fa8e2}
.footer-bar{left:130px;top:1070px;width:940px;height:50px;background:var(--green-bar);color:var(--white);font-size:11.3px;text-align:center;line-height:50px}
</style>
</head>
<body>

<header>
  <div class="abs brand">
    <span class="brand-mark"></span>
    <div>
      <div class="brand-name">AshworthMedical</div>
      <div class="brand-tag">Immediate Family and Personal Care</div>
    </div>
  </div>
  <div class="abs util-links"><span>&gt; Register</span><span>&gt; Login</span><span>&gt; Blog</span></div>
</header>

<nav class="abs main-nav">
  <ul>
    <li class="active">Home</li><li>About</li><li>Services</li><li>Staff</li><li>Insurance</li><li>Videos</li><li>Contact Us</li>
  </ul>
</nav>

<section>
  <div class="abs slider-bg"></div>
  <div class="abs slide-photo" role="img" aria-label="Photo of the clinic's doctors and staff smiling together"></div>
  <div class="abs slide-panel">
    <h2>Title of slide one</h2>
    <p>Lorem ipsum dolor sit amet, consectetur adipiscing elit. Praesent porttitor leo at lorem ultrices ac adipiscing mauris fringilla. Nunc vestibulum fermentum augue, ac blandit massa molestie quis. Aenean vestibulum sapien eget sapien viverra mollis.</p>
    <div class="slide-btn">
      <svg width="17" height="17" viewBox="0 0 17 17"><circle cx="8.5" cy="8.5" r="8.5" fill="#fff"/><path d="M4 8.5h7M8 5l3.5 3.5L8 12" stroke="#22b35e" stroke-width="2" fill="none"/></svg>
      Button
    </div>
  </div>
</section>

<aside class="abs care-box">
  <svg class="care-photo" viewBox="0 0 220 95" role="img" aria-label="Photo of a smiling family relaxing together">
    <defs><linearGradient id="famTone" x1="0" x2="1"><stop offset="0" stop-color="#c9a88c"/><stop offset=".5" stop-color="#e2cbb6"/><stop offset="1" stop-color="#b89478"/></linearGradient></defs>
    <path d="M0 0H220V95C170 70 90 110 0 60Z" fill="url(#famTone)"/>
    <path d="M0 60C90 110 170 70 220 95" stroke="#fff" stroke-width="3" fill="none"/>
  </svg>
  <h3>AREAS OF HEALTHCARE</h3>
  <ul>
    <li>Immediate Care</li><li>Allergies</li><li>Primary Care</li><li>Women’s Health</li><li>Medical Spa Treatments</li><li>Men’s Health</li><li>Weight Loss</li>
  </ul>
</aside>

<main>
  <h1 class="abs intro-title">We Care About the Health of You and Your Family</h1>
  <div class="abs intro-photo" role="img" aria-label="Photo of the clinic building exterior"></div>
  <div class="abs intro-text">
    <p>Lorem ipsum dolor sit amet, consectetur adipiscing elit. Praesent quis arcu nec mauris sagittis dapibus. Ut augue purus, varius ac molestie quis, egestas vel eros. Suspendisse potenti. Cras nec felis erat. Vestibulum elementum rutrum tellus, in aliquam metus tempus vel. Curabitur vulputate risus eu orci facilisis placerat. Duis pretium bibendum sapien eu elementum.</p>
    <p>Nunc varius sapien vitae felis aliquet a vestibulum dolor dapibus. Vestibulum eget semper magna. Etiam ut arcu erat, consectetur aliquam ligula.</p>
  </div>

  <div class="abs about-col" style="left:370px">
    <h4>It’s about time</h4>
    <p>Lorem ipsum dolor sit amet, consectetur adipiscing elit. Sed ut risus a massa varius viverra. In hac habitasse platea dictumst. Quisque faucibus pulvinar mi et luctus.</p>
    <p>Duis lacus augue, malesuada sed dignissim ut, tincidunt quis ante. Nunc</p>
  </div>
  <div class="abs about-col" style="left:610px">
    <h4>It’s about choices</h4>
    <p>Lorem ipsum dolor sit amet, consectetur adipiscing elit. Sed ut risus a massa varius viverra. In hac habitasse platea dictumst. Quisque faucibus pulvinar mi et luctus.</p>
    <p>Duis lacus augue, malesuada sed dignissim ut, tincidunt quis ante. Nunc</p>
  </div>
  <div class="abs about-col" style="left:850px">
    <h4>It’s about you</h4>
    <p>Lorem ipsum dolor sit amet, consectetur adipiscing elit. Sed ut risus a massa varius viverra. In hac habitasse platea dictumst. Quisque faucibus pulvinar mi et luctus.</p>
    <p>Duis lacus augue, malesuada sed dignissim ut, tincidunt quis ante. Nunc</p>
  </div>

  <div class="abs feature" style="left:129px">
    <h5>No Appointment? No Problem</h5><div class="rule"></div>
    <p>Lorem ipsum dolor sit amet, consectetur adipiscing elit.</p>
    <svg width="62" height="62" viewBox="0 0 62 62"><circle cx="31" cy="30" r="28" fill="#fff" stroke="#22b35e" stroke-width="3"/><rect x="19" y="23" width="24" height="16" rx="3" fill="#22b35e"/><rect x="26" y="19" width="10" height="5" rx="1.5" fill="none" stroke="#22b35e" stroke-width="2"/><path d="M31 27v8M27 31h8" stroke="#fff" stroke-width="2.5"/></svg>
  </div>
  <div class="abs feature" style="left:449px">
    <h5>Patient Check-In</h5><div class="rule"></div>
    <p>Lorem ipsum dolor sit amet, consectetur adipiscing elit.</p>
    <svg width="62" height="62" viewBox="0 0 62 62"><circle cx="31" cy="30" r="28" fill="#fff" stroke="#22b35e" stroke-width="3"/><path d="M23 22h12l5 5v13H23Z" fill="none" stroke="#22b35e" stroke-width="2"/><path d="M27 31h9M27 35h9" stroke="#22b35e" stroke-width="2"/><path d="M33 26l6-6 2 2-6 6h-2Z" fill="#22b35e"/></svg>
  </div>
  <div class="abs feature" style="left:769px">
    <h5>Health Insurance</h5><div class="rule"></div>
    <p>Lorem ipsum dolor sit amet, consectetur adipiscing elit.</p>
    <svg width="62" height="62" viewBox="0 0 62 62"><circle cx="31" cy="30" r="28" fill="#fff" stroke="#22b35e" stroke-width="3"/><path d="M22 22h12l5 5v13H22Z" fill="none" stroke="#22b35e" stroke-width="2"/><path d="M26 31h7M26 35h9" stroke="#22b35e" stroke-width="2"/><path d="M32 25a6 6 0 0 1 12 0Z" fill="#22b35e"/><path d="M38 25v6" stroke="#22b35e" stroke-width="1.5"/></svg>
  </div>
</main>

<footer>
  <div class="abs footer">
    <div class="foot-col" style="left:40px;width:240px">
      <h6>Here goes transparent logo</h6>
      Copyright ©2012 Ashworth Medical<br>All rights reserved.<br>Ashworth collects information you provide on this website. To learn more, please read the <a href="#">Privacy Policy</a>.
    </div>
    <div class="foot-sep" style="left:310px"></div>
    <div class="foot-col" style="left:350px;width:230px">
      <h6>Contact with Ashworth Medical</h6>
      <div style="font-weight:700;margin-bottom:10px">(555) 014 2290</div>
      <div style="font-weight:700;margin-bottom:10px">AshworthFamilyMedical.example</div>
      4120 Ashworth Ave (at Elm Row) Ste 210,<br>Dallas, TX 75201
    </div>
    <div class="foot-sep" style="left:600px"></div>
    <div class="foot-col" style="left:639px;width:260px">
      <h6>Connect with Ashworth Medical</h6>
      <div class="social"><span class="social-icon"></span><a href="#">Like us on Friendbook</a></div>
      <div class="social" style="align-items:flex-start"><span class="social-icon alt"></span><span style="line-height:26px"><a href="#">Follow us @ashworthmedical</a><br><a href="#">on Chirper</a></span></div>
    </div>
  </div>
  <div class="abs footer-bar">About Us| New Patients | Insurance &amp; Billing | Our Medical Clinic | Our Staff | FAQ | Sitemap | Contact Us | Privacy Policy</div>
</footer>

</body>
</html>
```